Screen design for customizable church app

I am building a customizable app for churches. I need the following screens designed:
1) Landing Screen
-- Text field to enter a code to join a organization
-- Button to register a new organization
2) Registration Screen
-- Text field to enter an organization name
-- Register button
-- Screen should indicate price/month and free trial for X days
3) Restricted (requires login) screen
4) Organization home screen
-- Dynamic menu options of the following types:
a) Contact Us/Form
b) Video List
c) Audio List
d) Documents List
e) Message/Chat Rooms
f) Map/Directions
g) Webpage

Plus permission based options:
h) Profile Settings
i) Notification Center
j) Admin Settings
k) Manage members
l) View Form Submissions

Low-fi/wireframe designs attached. No color scheme or branding has been established yet.

```html
<!DOCTYPE html>
<html lang="en">
<head>
<meta charset="utf-8">
<title>Church App Screens</title>
<link href="https://fonts.googleapis.com/css2?family=Roboto:wght@400;500;700&display=swap" rel="stylesheet">
<style>
:root{
  --orange:#fb9a4b;
  --orange-dark:#f3883a;
  --ink:#1d1f24;
  --grey:#555b63;
  --muted:#8a9099;
  --line:#e4e6ea;
  --bg:#eceef1;
  --screen:#ffffff;
  --chip:#dfe2e6;
}
*{box-sizing:border-box;margin:0;padding:0}
html,body{width:1200px;height:624px;overflow:hidden}
body{background:var(--bg);font-family:'Roboto',sans-serif;color:var(--ink);position:relative}
.screen{position:absolute;top:97px;width:200px;height:430px;background:var(--screen);border-radius:18px;overflow:hidden;box-shadow:0 6px 24px rgba(20,24,35,.12)}
.screen--landing{left:80px}
.screen--register{left:360px}
.screen--login{left:640px}
.screen--home{left:920px}
.abs{position:absolute}
.status{top:9px;left:12px;right:12px;display:flex;justify-content:space-between;font-size:7px;font-weight:500}
.status svg{display:block}
.topbar{top:26px;left:10px;right:10px;height:20px;display:flex;align-items:center;justify-content:space-between}
.topbar__title{font-size:11px;font-weight:500}
.topbar__btn{width:17px;height:17px;border-radius:50%;background:var(--chip);display:flex;align-items:center;justify-content:center}
.photo{left:0;right:0}
.photo--prayer{top:0;height:200px;background:linear-gradient(160deg,#c77a56 0%,#e7b08f 35%,#d9c7b6 65%,#ffffff 100%)}
.photo--crowd{bottom:0;height:190px;background:linear-gradient(180deg,#ffffff 0%,#b9a7c2 25%,#6d5a6a 55%,#8b5a3c 80%,#4a3a36 100%)}
.brand{display:flex;align-items:center;gap:7px;font-weight:400;color:var(--ink)}
.brand__mark{background:var(--orange);border-radius:3px}
.input{left:8px;right:12px;height:27px;border:1px solid var(--line);border-radius:2px;box-shadow:0 2px 6px rgba(0,0,0,.06);font-size:6.5px;color:var(--muted);padding-left:12px;display:flex;align-items:center;background:#fff}
.link{left:0;right:0;text-align:center;font-size:10px;font-weight:500;color:var(--orange);text-decoration:underline}
.btn{height:24px;border-radius:12px;background:var(--orange);color:#fff;font-size:8px;font-weight:500;display:flex;align-items:center;justify-content:center;letter-spacing:.2px}
.tile{width:81px;height:70px;background:#fff;border-radius:3px;box-shadow:0 2px 8px rgba(0,0,0,.09);display:flex;flex-direction:column;align-items:center;justify-content:center;gap:9px;font-size:8.5px;font-weight:500}
.tile--active{background:var(--orange);color:#fff}
.tile svg{width:30px;height:30px}
.fab{left:88px;top:388px;width:24px;height:24px;border-radius:50%;background:var(--orange);display:flex;align-items:center;justify-content:center}
</style>
</head>
<body>

<!-- Landing -->
<section class="screen screen--landing">
  <div class="abs photo photo--prayer" role="img" aria-label="Photo of hands folded in prayer over an open bible"></div>
  <div class="abs brand" style="top:205px;left:36px;font-size:20px"><span class="brand__mark" style="width:14px;height:14px"></span>Our Parish</div>
  <p class="abs" style="top:245px;left:8px;font-size:9.5px;font-weight:500;color:var(--grey)">Our Parish</p>
  <h1 class="abs" style="top:262px;left:8px;font-size:14.5px;font-weight:500">The Custom. Church App</h1>
  <p class="abs" style="top:297px;left:8px;font-size:7.5px">Enter a code to join an oranization.</p>
  <div class="abs input" style="top:312px">Enter a code</div>
  <a class="abs link" style="top:378px">Register an Organization</a>
</section>

<!-- Registration -->
<section class="screen screen--register">
  <div class="abs status"><span>12:00</span><svg width="30" height="7" viewBox="0 0 30 7"><rect x="0" y="4" width="2" height="3"/><rect x="3" y="3" width="2" height="4"/><rect x="6" y="1" width="2" height="6"/><path d="M11 3.5a4 4 0 0 1 6 0l-3 3z"/><rect x="20" y="1" width="9" height="5" rx="1"/></svg></div>
  <div class="abs topbar">
    <svg width="12" height="8" viewBox="0 0 12 8"><path d="M11 4H2M5 1 2 4l3 3" stroke="#1d1f24" stroke-width="1.4" fill="none"/></svg>
    <span class="topbar__title">Registration</span>
    <span class="topbar__btn"><svg width="7" height="7" viewBox="0 0 7 7"><circle cx="3.5" cy="2" r="1.6"/><path d="M.5 7a3 3 0 0 1 6 0z"/></svg></span>
  </div>
  <h2 class="abs" style="top:82px;left:8px;font-size:12.5px;font-weight:500">Registration Organization</h2>
  <p class="abs" style="top:118px;left:8px;font-size:7.5px">Church Name</p>
  <div class="abs input" style="top:133px">Enter a code</div>
  <div class="abs btn" style="top:176px;left:42px;width:110px">REGISTER</div>
  <p class="abs" style="top:211px;left:22px;font-size:9.5px;font-weight:500">$ 25.95<span style="font-size:6.5px;color:var(--muted)">/1month</span></p>
  <p class="abs" style="top:212px;left:96px;font-size:8px">Free trial for 7 days</p>
  <div class="abs photo photo--crowd" role="img" aria-label="Photo of a worship crowd with raised hands"></div>
</section>

<!-- Login required -->
<section class="screen screen--login">
  <div class="abs status"><span>12:00</span><svg width="30" height="7" viewBox="0 0 30 7"><rect x="0" y="4" width="2" height="3"/><rect x="3" y="3" width="2" height="4"/><rect x="6" y="1" width="2" height="6"/><path d="M11 3.5a4 4 0 0 1 6 0l-3 3z"/><rect x="20" y="1" width="9" height="5" rx="1"/></svg></div>
  <div class="abs topbar">
    <svg width="12" height="8" viewBox="0 0 12 8"><path d="M11 4H2M5 1 2 4l3 3" stroke="#1d1f24" stroke-width="1.4" fill="none"/></svg>
    <span class="topbar__title">Login Required</span>
    <span class="topbar__btn"><svg width="7" height="6" viewBox="0 0 7 6"><path d="M0 .5h7M0 3h7M0 5.5h7" stroke="#1d1f24" stroke-width="1"/></svg></span>
  </div>
  <div class="abs brand" style="top:120px;left:20px;font-size:24px"><span class="brand__mark" style="width:16px;height:16px"></span>Our Parish</div>
  <svg class="abs" style="top:180px;left:78px" width="44" height="44" viewBox="0 0 44 44">
    <path d="M12 18v-6a10 10 0 0 1 20 0v6" fill="none" stroke="#1d1f24" stroke-width="2.4"/>
    <rect x="3" y="18" width="38" height="22" rx="3" fill="#fff" stroke="#1d1f24" stroke-width="2.4"/>
    <rect x="3" y="24" width="38" height="9" fill="#fff" stroke="#1d1f24" stroke-width="2"/>
    <text x="7" y="32" font-size="9" fill="#fb9a4b" font-family="Roboto,sans-serif" font-weight="700">* * * *</text>
  </svg>
  <h2 class="abs" style="top:236px;left:0;right:0;text-align:center;font-size:13px;font-weight:500">Login Required</h2>
  <div class="abs btn" style="top:267px;left:20px;width:156px">LOGIN</div>
  <a class="abs link" style="top:380px">Register an Organization</a>
</section>

<!-- Organization home -->
<section class="screen screen--home">
  <div class="abs status"><span>12:00</span><svg width="30" height="7" viewBox="0 0 30 7"><rect x="0" y="4" width="2" height="3"/><rect x="3" y="3" width="2" height="4"/><rect x="6" y="1" width="2" height="6"/><path d="M11 3.5a4 4 0 0 1 6 0l-3 3z"/><rect x="20" y="1" width="9" height="5" rx="1"/></svg></div>
  <div class="abs topbar">
    <svg width="12" height="8" viewBox="0 0 12 8"><path d="M11 4H2M5 1 2 4l3 3" stroke="#1d1f24" stroke-width="1.4" fill="none"/></svg>
    <span class="topbar__title">Organization</span>
    <span class="topbar__btn"><svg width="7" height="7" viewBox="0 0 7 7"><circle cx="3.5" cy="2" r="1.6"/><path d="M.5 7a3 3 0 0 1 6 0z"/></svg></span>
  </div>

  <div class="abs tile tile--active" style="top:61px;left:10px">
    <svg viewBox="0 0 30 30" fill="none" stroke="#fff" stroke-width="1.6"><rect x="3" y="3" width="24" height="24"/><path d="M3 8h24M7 13h16M7 17h10M7 21h16"/></svg>
    Contact Us/Form
  </div>
  <div class="abs tile" style="top:61px;left:109px">
    <svg viewBox="0 0 30 30" fill="none" stroke="#fb9a4b" stroke-width="1.6"><rect x="3" y="3" width="24" height="24"/><path d="M8 9v8l6-4z"/><path d="M18 8h5M18 12h5M18 16h5M6 21h5M13 21h5M20 21h3"/></svg>
    Video List
  </div>
  <div class="abs tile" style="top:145px;left:10px">
    <svg viewBox="0 0 30 30" fill="none" stroke="#fb9a4b" stroke-width="1.8"><rect x="8" y="4" width="14" height="16"/><path d="M3 7v10M27 7v10M5 24h22"/><path d="M17 8v8M17 8l-3 1M17 16a2 2 0 1 1-2-2" /><circle cx="12" cy="24" r="2" fill="#fb9a4b"/></svg>
    Audio List
  </div>
  <div class="abs tile" style="top:145px;left:109px">
    <svg viewBox="0 0 30 30" fill="#fb9a4b"><path d="M7 2h11l6 6v20H7z"/><path d="M10 13h2v2h-2zM14 13h8v2h-8zM10 18h2v2h-2zM14 18h8v2h-8zM10 23h2v2h-2zM14 23h8v2h-8z" fill="#fff"/></svg>
    Documents List
  </div>
  <div class="abs tile" style="top:229px;left:10px">
    <svg viewBox="0 0 30 30"><path d="M4 12a9 8 0 1 1 5 7l-5 2 2-4a8 8 0 0 1-2-5z" fill="#fb9a4b"/><path d="M11 15a9 8 0 1 1 5 7l-4 3 1-4a8 8 0 0 1-2-6z" fill="#fff" stroke="#fb9a4b" stroke-width="1.6"/><circle cx="16" cy="16" r="1" fill="#fb9a4b"/><circle cx="20" cy="16" r="1" fill="#fb9a4b"/><circle cx="24" cy="16" r="1" fill="#fb9a4b"/></svg>
    Chat Rooms
  </div>
  <div class="abs tile" style="top:229px;left:109px">
    <svg viewBox="0 0 30 30" fill="none" stroke="#fb9a4b" stroke-width="1.8"><path d="M15 22s-7-7-7-12a7 7 0 0 1 14 0c0 5-7 12-7 12z" fill="#fb9a4b"/><circle cx="15" cy="10" r="2.4" fill="#fff" stroke="none"/><path d="M8 20l-5 7h24l-5-7"/></svg>
    Map/Directions
  </div>
  <div class="abs tile" style="top:313px;left:60px">
    <svg viewBox="0 0 30 30" fill="none" stroke="#fb9a4b" stroke-width="1.6"><circle cx="15" cy="15" r="12"/><ellipse cx="15" cy="15" rx="5" ry="12"/><path d="M3 15h24M5 9h20M5 21h20"/></svg>
    Webpage
  </div>
  <div class="abs fab"><svg width="10" height="10" viewBox="0 0 10 10"><path d="M5 0v10M0 5h10" stroke="#fff" stroke-width="2"/></svg></div>
</section>

</body>
</html>
```